Lanterne architecture business cards

We are a new company based in New Zealand. We Specialize in High end Luxury Residential Architecture.

Every home is bespoke and is designed to each clients individual requirements and needs.

I like to design buildings that inspire people through light and form while offering a high level of comfort and usability.

Lines of sight, proportion and balance are fundamental to the spaces I create.
Updates

August 5th is current deadline - Today's date is the 13th of August.

Target Market(s)

New Zealanders who want a custom individual home design, typically 30-65 year old males and females

Industry/Entity Type

Architecture

Contact Information for Business Card

Director - Derek Tolson
Contact Number - 0279164073
Email - info@lanternearchitecture-example.co.nz
Webstie - www.lanternearchitecture-example.co.nz
Social Media - @lanternearchitecture

Font styles to use
Sans Serif

Requirements
Must have
• Logo (Both Sides)
Website
Email
Contact Number
Social Media

Nice to have
• Texture
Should not have
• More than 3 colours - typically I would've thought 2 would be good to match the logo.

```html
<!DOCTYPE html>
<html lang="en">
<head>
<meta charset="utf-8">
<title>Lanterne Architecture – Business Cards</title>
<link rel="stylesheet" href="https://fonts.googleapis.com/css2?family=Poppins:wght@300;400;600&display=swap">
<style>
  :root {
    --backdrop: #d8d8d8;
    --card: #f6f6f5;
    --ink: #111111;
    --deboss: #e6e6e4;
    --rule: #3a3a3a;
  }
  * { margin: 0; padding: 0; box-sizing: border-box; }
  html, body {
    width: 1200px;
    height: 800px;
    overflow: hidden;
    background: var(--backdrop);
    font-family: "Poppins", sans-serif;
    color: var(--ink);
  }
  .canvas { position: relative; width: 1200px; height: 800px; }

  .card {
    position: absolute;
    top: 283px;
    width: 430px;
    height: 240px;
    background: var(--card);
  }
  .card--front { left: 110px; }
  .card--back { left: 638px; }

  /* Front: debossed brand name */
  .front-mark {
    position: absolute;
    inset: 0;
    display: flex;
    align-items: center;
    justify-content: center;
    font-weight: 300;
    font-size: 46px;
    letter-spacing: 2px;
    color: var(--deboss);
  }

  /* Back: brand block */
  .brand {
    position: absolute;
    right: 26px;
    top: 26px;
    display: flex;
    flex-direction: column;
    align-items: flex-end;
    font-weight: 400;
    color: var(--ink);
  }
  .brand__dot {
    width: 30px;
    height: 30px;
    border-radius: 50%;
    border: 3px solid var(--ink);
    margin-right: 64px;
    margin-bottom: 18px;
  }
  .brand__name {
    font-size: 17px;
    letter-spacing: 6.2px;
    line-height: 1;
  }
  .brand__sub {
    margin-top: 3px;
    font-size: 5px;
    letter-spacing: 6.6px;
    line-height: 1;
  }

  .person {
    position: absolute;
    left: 28px;
    top: 131px;
  }
  .person__name {
    font-weight: 600;
    font-size: 11px;
    letter-spacing: 0.3px;
    line-height: 14px;
  }
  .person__role {
    font-size: 9px;
    line-height: 12px;
    letter-spacing: 0.3px;
  }

  .divider {
    position: absolute;
    left: 28px;
    right: 28px;
    top: 166px;
    border-top: 1px solid var(--rule);
  }

  .contacts {
    position: absolute;
    left: 28px;
    top: 175px;
    list-style: none;
  }
  .contacts li {
    display: flex;
    align-items: center;
    gap: 5px;
    height: 16px;
    font-size: 10px;
    letter-spacing: 0.2px;
  }
  .contacts svg { width: 8px; height: 8px; flex: none; }

  .social {
    position: absolute;
    right: 28px;
    top: 175px;
    height: 16px;
    display: flex;
    align-items: center;
    gap: 4px;
    font-size: 10px;
    letter-spacing: 0.2px;
  }
  .social__handle { margin-right: 2px; }
  .social__badge {
    width: 11px;
    height: 11px;
    border-radius: 50%;
    background: var(--ink);
  }
</style>
</head>
<body>
<main class="canvas">

  <section class="card card--front" aria-label="Business card front">
    <div class="front-mark">lanterne</div>
  </section>

  <section class="card card--back" aria-label="Business card back">
    <div class="brand">
      <span class="brand__dot" aria-hidden="true"></span>
      <span class="brand__name">LANTERNE</span>
      <span class="brand__sub">ARCHITECTURE</span>
    </div>

    <div class="person">
      <p class="person__name">DEREK TOLSON</p>
      <p class="person__role">DIRECTOR</p>
    </div>

    <div class="divider"></div>

    <ul class="contacts">
      <li>
        <svg viewBox="0 0 10 10" aria-hidden="true"><path d="M2 0.6 L3.6 0.6 L4.3 2.8 L3.2 3.7 C3.8 5 5 6.2 6.3 6.8 L7.2 5.7 L9.4 6.4 L9.4 8 C9.4 9 8.6 9.6 7.6 9.4 C4.2 8.7 1.3 5.8 0.6 2.4 C0.4 1.4 1 0.6 2 0.6 Z" fill="currentColor"/></svg>
        <span>0279164073</span>
      </li>
      <li>
        <svg viewBox="0 0 10 10" aria-hidden="true"><rect x="0.5" y="2" width="9" height="6.4" rx="0.6" fill="currentColor"/><path d="M0.8 2.4 L5 5.6 L9.2 2.4" stroke="#f6f6f5" stroke-width="0.9" fill="none"/></svg>
        <span>info@lanternearchitecture-example.co.nz</span>
      </li>
      <li>
        <svg viewBox="0 0 10 10" aria-hidden="true"><circle cx="5" cy="5" r="4.5" fill="currentColor"/><g stroke="#f6f6f5" stroke-width="0.7" fill="none"><ellipse cx="5" cy="5" rx="2" ry="4.3"/><path d="M0.6 5 H9.4 M1.3 2.8 H8.7 M1.3 7.2 H8.7"/></g></svg>
        <span>www.lanternearchitecture-example.co.nz</span>
      </li>
    </ul>

    <div class="social">
      <span class="social__handle">@lanternearchitecture</span>
      <span class="social__badge" aria-hidden="true"></span>
      <span class="social__badge" aria-hidden="true"></span>
      <span class="social__badge" aria-hidden="true"></span>
    </div>
  </section>

</main>
</body>
</html>
```